Wickedmarlo.com adult webpage with links to various sites she is on.

UPDATE 3/10- let’s keep this a bit more simple. I am uploading three pics and a sketch of how she wants her site to look. It’s really just a page that has her links.

Looking to set up a homepage for my hot wife that has her clickable links on there. Pehaps a space for an about me and some notes encouraging audience to click and join peek vault.
Cashwix link:

https://peekvault.com/away?url=https://Cashwix.com/wickedmarlo

Here is some
Copy from her:
“Queen of Dirty Talk” is important to work in.
🔥HOTWIFE SUPER SLUT🔥

...... I do things the other girls don’t! I suck and fuck like no other woman you’ll ever see. Filthy dirty talk, lots of sloppy oral, fantasy role play, dress up and cum swallowing.

Cum watch me! Have your mind..... and your big fat load blown away!

💋This page is where you will find ALL my links. My free peekvault has my videos for sale. My VIP page you will get the same videos at a discounted prices, plus lots of juicy extras. I also answer all my messages there. Make sure to check out my VIP page today so you don’t miss out on any of the fun!💋💋💋
Updates

I am tryin go to extend the project time to at least two weeks. I just don’t know how to edit. I have an email out to support.

Target Market(s)

Adult entertainment

Industry/Entity Type

Porn

Coding

Coded - Design and coding required

Number of Pages Required

1 page

Colors
000000
eea4c8

Requirements
Must have
• WickedMarlo (no space between) is her stage name.
She would like maybe some cute horns in the logo. Maybe make the “S” have little devil horns on top and roll the bottom of the “S” like a devil tail with the arrows/spade point at at end.
A hot pic of her in background.
Buttons to her various pages.
Nice to have
• Perhaps an about me drop down or window we can write copy for? Pink black and leopard are good color choices.

```html
<!DOCTYPE html>
<html lang="en">
<head>
<meta charset="utf-8">
<title>WickedMarlo</title>
<link rel="stylesheet" href="https://fonts.googleapis.com/css2?family=Playball&family=Cinzel+Decorative:wght@700&family=Work+Sans:wght@400;500;600&display=swap">
<style>
  :root {
    --pink: #eea4c8;
    --black: #000000;
    --ink: #1b1b1b;
    --white: #ffffff;
    --muted: #b9b9b9;
    --rule: #3a3a3a;
    --btn-blue: #3f6597;
    --btn-sky: #1a9be0;
    --btn-red: #e0241b;
  }
  * { box-sizing: border-box; margin: 0; padding: 0; }
  html, body { width: 796px; height: 1200px; overflow: hidden; }
  body { font-family: "Work Sans", Arial, sans-serif; background: var(--white); color: var(--ink); position: relative; }

  .hero { position: absolute; left: 0; top: 0; width: 796px; height: 345px;
    background: linear-gradient(100deg, #1d1d1d 0%, #6c6c6c 30%, #bdbdbd 55%, #8a8a8a 75%, #2a2a2a 100%); }
  .wordmark { font-family: "Work Sans", Arial, sans-serif; font-weight: 600; color: var(--pink);
    line-height: 1; white-space: nowrap; letter-spacing: .5px; }
  .hero-logo { position: absolute; top: 52px; left: 0; width: 100%; text-align: center; font-size: 50px; }

  .about { position: absolute; left: 0; top: 345px; width: 796px; height: 435px; background: var(--white); }
  .portrait-frame { position: absolute; left: 66px; top: 47px; width: 228px; height: 364px;
    border: 1px solid #cfcfcf; padding: 12px; }
  .portrait { width: 100%; height: 100%; border: 2px solid var(--pink);
    background: radial-gradient(ellipse at 45% 45%, #d9d9d9 0%, #9a9a9a 55%, #4a4a4a 100%); }

  .about-body { position: absolute; left: 403px; top: 70px; width: 322px; }
  .about-title { font-family: "Cinzel Decorative", serif; font-size: 34px; color: var(--black); line-height: 1; }
  .about-title span { font-family: "Playball", cursive; font-weight: 400; color: var(--pink); font-size: 38px; }
  .about-copy { margin-top: 14px; font-size: 10.6px; line-height: 1.65; color: #333; }

  .links { margin-top: 20px; }
  .link-row { display: flex; gap: 10px; margin-bottom: 12px; }
  .btn { display: flex; align-items: center; justify-content: center; gap: 6px; height: 28px;
    border-radius: 14px; color: var(--white); font-size: 10px; font-weight: 600; letter-spacing: .5px; text-decoration: none; }
  .btn-wide { width: 156px; }
  .btn-small { width: 100px; }
  .btn-vip { background: var(--pink); }
  .btn-free { background: var(--black); }
  .btn-picshare { background: var(--btn-blue); }
  .btn-chirp { background: var(--btn-sky); }
  .btn-stream { background: var(--btn-red); }
  .dot { width: 7px; height: 7px; border-radius: 50%; background: var(--white); }

  .footer { position: absolute; left: 0; top: 780px; width: 796px; height: 420px;
    background: linear-gradient(180deg, #101010, #1c1c1c); color: var(--white); }
  .news-title { position: absolute; top: 28px; width: 100%; text-align: center;
    font-family: "Playball", cursive; font-size: 38px; font-weight: 400; }
  .news-text { position: absolute; top: 88px; width: 100%; text-align: center; font-size: 11px; color: #ddd; }
  .news-form { position: absolute; left: 199px; top: 122px; width: 398px; height: 38px;
    border: 1px solid #777; border-radius: 19px; display: flex; align-items: center; padding: 0 4px 0 20px; }
  .news-input { flex: 1; font-size: 11px; color: #cfcfcf; }
  .news-btn { width: 100px; height: 30px; border-radius: 15px; background: var(--pink);
    display: flex; align-items: center; justify-content: center; font-size: 10px; font-weight: 600; letter-spacing: 1px; }
  .rule { position: absolute; left: 66px; width: 664px; height: 1px; background: var(--rule); }
  .footer-logo { position: absolute; left: 66px; top: 238px; font-size: 26px; }
  .col { position: absolute; top: 226px; }
  .col h4 { font-size: 12px; font-weight: 600; letter-spacing: .5px; margin-bottom: 10px; }
  .col li { list-style: none; font-size: 8.5px; color: var(--muted); line-height: 13px; letter-spacing: .3px; }
  .copyright { position: absolute; top: 386px; width: 100%; text-align: center; font-size: 10px; color: #ccc; }
</style>
</head>
<body>
  <header class="hero" role="img" aria-label="Black and white photo of the model lying on a striped bed">
    <div class="wordmark hero-logo">WickedMarlo</div>
  </header>

  <section class="about">
    <div class="portrait-frame">
      <div class="portrait" role="img" aria-label="Black and white portrait of the model"></div>
    </div>
    <div class="about-body">
      <h2 class="about-title">About <span>Me</span></h2>
      <p class="about-copy">Lorem ipsum dolor sit amet, conse adipiscing elit do eiusmod tempor incididunt ut labore et dolore magna ipe ipsum suspendisse gravida. Risus commodo viverra lacus vel facilisis. Lorem ipsum dolor sit amet, cor adipiscing elit, sed do eiusmod tempor incididunt ut labore et dolore magna aliqua. Quis ipsum suspendisse ultrices gravida. Risus commodo viverra maecenas accumsan lac vel facilisis. Lorem ipsum dolor sit amet, consectetur adipiscing elit do eiusmod tempor incididunt ut labore et dolore magna aliqua.</p>
      <nav class="links">
        <div class="link-row">
          <a class="btn btn-wide btn-vip" href="#"><span class="dot"></span>VIP</a>
          <a class="btn btn-wide btn-free" href="#"><span class="dot"></span>FREE</a>
        </div>
        <div class="link-row">
          <a class="btn btn-small btn-picshare" href="#"><span class="dot"></span>PICSHARE</a>
          <a class="btn btn-small btn-chirp" href="#"><span class="dot"></span>CHIRPLINE</a>
          <a class="btn btn-small btn-stream" href="#"><span class="dot"></span>STREAMTUBE</a>
        </div>
      </nav>
    </div>
  </section>

  <footer class="footer">
    <h3 class="news-title">Sign For Newsletter</h3>
    <p class="news-text">Receive weekly information about new arrivals, latest trends, events, brand news, and more.</p>
    <div class="news-form">
      <span class="news-input">Enter Email Address</span>
      <span class="news-btn">SUBSCRIBE</span>
    </div>
    <div class="rule" style="top:187px"></div>
    <div class="wordmark footer-logo">WickedMarlo</div>
    <div class="col" style="left:318px">
      <h4>OUR WORLD</h4>
      <ul><li>ABOUT US</li><li>OUR MODELS</li><li>OFFERS</li><li>SEX TOURS</li><li>POPULAR CELEBRITIES</li></ul>
    </div>
    <div class="col" style="left:464px">
      <h4>CUSTOMER CARE</h4>
      <ul><li>PAYMENT</li><li>DELIVERY AND RETURNS</li><li>GUIDE</li><li>HEALTH TESTING</li><li>FAQ</li><li>CONTACT US</li></ul>
    </div>
    <div class="col" style="left:623px">
      <h4>CORPORATE INFO</h4>
      <ul><li>IMPRINT</li><li>PRIVACY POLICY</li><li>TERMS AND CONDITIONS</li><li>STOP FAKE</li></ul>
    </div>
    <div class="rule" style="top:367px"></div>
    <p class="copyright">© 2021 WickedMarlo. All Rights Reserved.</p>
  </footer>
</body>
</html>
```